'Bright Ledger Hidden Keys' Book Cover

I need a professional book cover design for my new upcoming book that shows people how to get a high credit score.

Here are my two websites:

https://www.moneywordbank-lexa.info
https://moneywordbank-lexa.com/

I am looking for a clean, professional design that pops (emotional touch) and separates from the other books that are on the market. Cover aspect ratio 1:4 for Pagewisp version and 1:5 for the paperback version. Yellow or blue are good colors - but not must. See the basic examples that I provided. File delivery format PDF.

Book Title: Bright Ledger Hidden Keys
Byline: The Quick Lift And Mend Manual for Stellar Borrowing

Currently on Brindlecart pre-order:
https://www.brindlecart.example/Bright-Ledger-Hidden-Keys-Stellar-ebook/dp/Q48MPLRT71

I am the author of 36 published books on Brindlecart. My author profile is here:
brindlecart.example/author/gideonvarly

Targeted audience: People that want to improve or repair their bad credit score.

Target Market(s)

People/consumers in the US that want to improve or repair their credit score.

Industry/Entity Type

Consumer

Font styles to use
Sans Serif

Colors

Designer to choose colors to be used in the design.

Requirements
Must have
• Author name, Title, byline, and graphic element(s).
Nice to have
• - 2020 edition logo / batch

```html
<!DOCTYPE html>
<html lang="en">
<head>
<meta charset="utf-8">
<title>Bright Ledger Hidden Keys – Book Cover</title>
<link rel="stylesheet" href="https://fonts.googleapis.com/css2?family=Oswald:wght@500;600;700&display=swap">
<style>
  :root {
    --sky-top: #1f6fc4;
    --sky-mid: #1558b0;
    --sky-deep: #0b2e78;
    --glow: #5fc8f5;
    --title-yellow: #f6e31c;
    --title-blue: #63c9f3;
    --text-white: #ffffff;
    --badge-ink: #123f8c;
  }
  html, body {
    margin: 0;
    padding: 0;
    width: 857px;
    height: 1200px;
    overflow: hidden;
    background: var(--sky-deep);
  }
  .cover {
    position: relative;
    width: 857px;
    height: 1200px;
    overflow: hidden;
    font-family: 'Oswald', 'Arial Narrow', sans-serif;
    background: linear-gradient(180deg, var(--sky-top) 0%, var(--sky-mid) 45%, var(--sky-deep) 100%);
  }
  .hero-visual {
    position: absolute;
    left: 110px;
    top: 300px;
    width: 760px;
    height: 660px;
    background:
      radial-gradient(ellipse 45% 35% at 62% 42%, rgba(210, 240, 255, 0.85) 0%, rgba(95, 200, 245, 0.55) 40%, rgba(31, 111, 196, 0) 75%),
      radial-gradient(ellipse 30% 40% at 25% 70%, rgba(95, 200, 245, 0.45) 0%, rgba(31, 111, 196, 0) 70%);
  }
  .title {
    position: absolute;
    left: 0;
    right: 0;
    margin: 0;
    text-align: center;
    font-weight: 700;
    text-transform: uppercase;
    line-height: 1;
  }
  .title-line-one {
    top: 70px;
    font-size: 112px;
    color: var(--title-yellow);
  }
  .title-line-two {
    top: 190px;
    font-size: 98px;
    color: var(--title-blue);
    letter-spacing: 1px;
  }
  .subtitle {
    position: absolute;
    left: 92px;
    top: 330px;
    margin: 0;
    font-weight: 600;
    font-size: 40px;
    line-height: 1.2;
    text-transform: uppercase;
    color: var(--title-yellow);
  }
  .subtitle .accent { color: var(--title-blue); }
  .subtitle .plain { color: var(--text-white); }
  .edition-badge {
    position: absolute;
    left: 680px;
    top: 752px;
    width: 168px;
    height: 168px;
    border-radius: 50%;
    background: var(--title-yellow);
    display: flex;
    flex-direction: column;
    align-items: center;
    justify-content: center;
    transform: rotate(-18deg);
    color: var(--badge-ink);
    font-weight: 700;
    line-height: 1;
  }
  .edition-year { font-size: 52px; }
  .edition-label { font-size: 32px; letter-spacing: 1px; }
  .author {
    position: absolute;
    left: 0;
    right: 0;
    top: 950px;
    margin: 0;
    text-align: center;
    font-weight: 700;
    font-size: 124px;
    line-height: 1;
    color: var(--title-yellow);
    text-transform: uppercase;
  }
  .series {
    position: absolute;
    left: 0;
    right: 0;
    top: 1110px;
    margin: 0;
    text-align: center;
    font-weight: 500;
    font-size: 40px;
    color: var(--text-white);
  }
</style>
</head>
<body>
  <main class="cover">
    <div class="hero-visual" role="img" aria-label="Photo of a hand holding a credit card in glowing blue light"></div>

    <h1 class="title title-line-one">Bright Ledger</h1>
    <h1 class="title title-line-two">Hidden Keys</h1>

    <p class="subtitle">
      The Quick Lift And<br>
      <span class="accent">Mend</span> <span class="plain">Manual</span><br>
      For Stellar Borrowing
    </p>

    <div class="edition-badge">
      <span class="edition-year">2020</span>
      <span class="edition-label">EDITION</span>
    </div>

    <p class="author">Gideon Varly</p>
    <p class="series">Varly Financial Literacy Program</p>
  </main>
</body>
</html>
```